I need a folder to put papers in when I am scheduling patients for surgery. The information is general, such as costs, consent forms etc. The folder is designed to give the patient these papers in a neat manner. The cover of the folder needs to use my brand and perhaps create some interest when it is sitting on their kitchen bench with visitors and family. I'll attach a typical template for a folder. It needs to be stylish, classic and professional, as I am about to operate on the person's eye. <br/>I would like my logo included. I'll also attach a photo which is on my website which might work to wrap around the folder. The website address is bramwelkoske.com.au and you can see the way the image is used there on most of the pages as a banner. My profile photo could possibly used as well. Perhaps on the back, but if it looks strange then that is not necessary. The contact information need not be on the folder. Just Dr Lars Brimwell, Ophthalmic Surgeon. Finally, our brand slogan is. "The world's a beautiful place, see it clearly". This could also be on it. Again, this all needs to be professional looking. <br/>I've attached all our previous design jobs, 2 profile pictures, and the image that I think would work. Please also look at the website. <br/><br/>The second part of the project is to create a business card for my practice manager. Her name is Fiona Pelkrest<br/>It should include<br/>Fiona Pelkrest (BCom)<br/>Practice Manager for Dr Lars Brimwell<br/>Ophthalmic Surgeon <br/><br/>Then all the details which are on our current business card<br/><br/><br/><br/><br/>

Contact Information for Business Card

Just match the business cards I already have, but use the details above

Colors

Designer to choose colors to be used in the design.

```html
<!DOCTYPE html>
<html lang="en">
<head>
<meta charset="utf-8">
<title>Fiona Pelkrest – Business Card</title>
<link rel="stylesheet" href="https://fonts.googleapis.com/css2?family=Lato:wght@300;400;700&display=swap">
<style>
  :root {
    --name-blue: #3ba7da;
    --text-grey: #55575c;
    --icon-blue: #0b6fae;
    --paper: #ffffff;
  }
  html, body { margin: 0; padding: 0; overflow: hidden; background: var(--paper); }
  .card {
    position: relative;
    width: 1200px;
    height: 686px;
    overflow: hidden;
    background: var(--paper);
    font-family: "Lato", sans-serif;
  }
  .card__backdrop { position: absolute; inset: 0; width: 1200px; height: 686px; }
  .card__name {
    position: absolute; left: 0; width: 1200px; top: 130px; margin: 0;
    text-align: center; font-weight: 700; font-size: 54px; letter-spacing: 1px;
    color: var(--name-blue); line-height: 1;
  }
  .card__degree {
    position: absolute; left: 0; width: 1200px; top: 188px; margin: 0;
    text-align: center; font-weight: 300; font-size: 33px; letter-spacing: 2px;
    color: var(--name-blue); line-height: 1;
  }
  .card__role {
    position: absolute; left: 0; width: 1200px; top: 222px; margin: 0;
    text-align: center; font-weight: 300; font-size: 34px; letter-spacing: 3px;
    color: var(--text-grey); line-height: 39px;
  }
  .contact {
    position: absolute; display: flex; align-items: center; gap: 10px;
    font-weight: 300; color: var(--text-grey); letter-spacing: 4px; font-size: 36px;
    line-height: 1;
  }
  .contact--phone { left: 438px; top: 351px; }
  .contact--fax { left: 442px; top: 419px; }
  .contact--email { left: 324px; top: 483px; font-size: 34px; letter-spacing: 3.2px; gap: 8px; }
  .contact__icon { display: block; flex: none; }
</style>
</head>
<body>
<div class="card">
  <svg class="card__backdrop" viewBox="0 0 1200 686" aria-hidden="true">
    <defs>
      <linearGradient id="cornerDeep" x1="0" y1="0" x2="1" y2="1">
        <stop offset="0" stop-color="#7dbcff"/>
        <stop offset="1" stop-color="#1565e8"/>
      </linearGradient>
      <linearGradient id="cornerSoft" x1="0" y1="0" x2="1" y2="1">
        <stop offset="0" stop-color="#ffffff"/>
        <stop offset="1" stop-color="#bfe6ff"/>
      </linearGradient>
      <linearGradient id="waveDeep" x1="0" y1="0" x2="1" y2="1">
        <stop offset="0" stop-color="#3f8ff5"/>
        <stop offset="1" stop-color="#42c6ff"/>
      </linearGradient>
      <linearGradient id="waveSoft" x1="0" y1="0" x2="1" y2="1">
        <stop offset="0" stop-color="#d6e9fd"/>
        <stop offset="1" stop-color="#ffffff"/>
      </linearGradient>
    </defs>

    <path d="M690 0 H1200 V330 C1110 250 1010 150 930 80 C870 30 790 6 690 0 Z" fill="url(#cornerSoft)"/>
    <path d="M820 0 H1200 V250 C1120 190 1050 120 990 62 C945 20 890 4 820 0 Z" fill="url(#cornerDeep)"/>
    <path d="M1020 310 C1090 370 1150 430 1200 490 V560 C1140 490 1070 420 1000 360 Z" fill="#e3f0fe"/>

    <path d="M0 330 C170 390 320 510 430 686 H0 Z" fill="url(#waveSoft)"/>
    <path d="M0 420 C130 460 240 560 320 686 H0 Z" fill="url(#waveDeep)"/>
    <path d="M0 140 C90 170 170 220 230 280 C150 250 70 230 0 225 Z" fill="#e6f1fd"/>
  </svg>

  <h1 class="card__name">FIONA PELKREST</h1>
  <p class="card__degree">(B.Com)</p>
  <p class="card__role">Practice Manager for<br>Dr. Lars Brimwell<br>Ophthalmatic Surgeon</p>

  <div class="contact contact--phone">
    <svg class="contact__icon" width="56" height="56" viewBox="0 0 56 56" aria-hidden="true">
      <circle cx="28" cy="28" r="27" fill="var(--icon-blue)"/>
      <circle cx="28" cy="28" r="23" fill="none" stroke="#fff" stroke-width="2"/>
      <path d="M22 16 q-4 2 -3 8 q2 9 10 16 q5 3 8 0 l1.5 -2 -5 -5 -3 2 q-5 -4 -6 -9 l3 -2 -2 -7 z" fill="#fff"/>
    </svg>
    <span>(08) 9471 2605</span>
  </div>

  <div class="contact contact--fax">
    <svg class="contact__icon" width="48" height="48" viewBox="0 0 48 48" aria-hidden="true">
      <circle cx="24" cy="24" r="23" fill="var(--icon-blue)"/>
      <circle cx="24" cy="24" r="19.5" fill="none" stroke="#fff" stroke-width="1.8"/>
      <rect x="15" y="13" width="18" height="9" rx="1.5" fill="none" stroke="#fff" stroke-width="2.4"/>
      <rect x="11" y="21" width="26" height="14" rx="3" fill="#fff"/>
      <rect x="17" y="26" width="14" height="4" fill="var(--icon-blue)"/>
    </svg>
    <span>(08) 9471 2618</span>
  </div>

  <div class="contact contact--email">
    <svg class="contact__icon" width="38" height="38" viewBox="0 0 38 38" aria-hidden="true">
      <g fill="none" stroke="var(--icon-blue)" stroke-width="3">
        <circle cx="19" cy="19" r="17"/>
        <ellipse cx="19" cy="19" rx="7.5" ry="17"/>
        <line x1="19" y1="2" x2="19" y2="36"/>
        <line x1="2" y1="19" x2="36" y2="19"/>
        <path d="M5 10 H33 M5 28 H33"/>
      </g>
    </svg>
    <span>reception@bramwelkoske.com.au</span>
  </div>
</div>
</body>
</html>
```